Summer Fun

I need a Poster for Front of hotel advertising discounted drinks on Thursday & Fridays
$3.50.
Schooners of Local Beer, Glass of House Wine & Bubbly.
From 3.30pm to 6.30 pm
Nibblies Provided

Target Market(s)

25 + Market

Industry/Entity Type

Hotel

Requirements
Should not have
• Do not want to be known as Happy Hour.

```html
<!DOCTYPE html>
<html lang="en">
<head>
<meta charset="utf-8">
<title>Cheap Drinks – Thursday &amp; Friday</title>
<link rel="stylesheet" href="https://fonts.googleapis.com/css2?family=Arimo:ital,wght@0,400;0,700;1,700&family=Chewy&display=swap">
<style>
  :root {
    --frame-red: #961325;
    --deep-red: #c81f36;
    --warm-red: #dc3a32;
    --sun-orange: #f5931d;
    --leaf-red: #a8182c;
    --headline-yellow: #fff200;
    --text-white: #ffffff;
  }
  html, body {
    margin: 0;
    padding: 0;
    width: 849px;
    height: 1200px;
    overflow: hidden;
    background: var(--frame-red);
  }
  .poster {
    position: relative;
    width: 849px;
    height: 1200px;
    background: var(--frame-red);
    font-family: "Arimo", Arial, sans-serif;
  }
  .poster__panel {
    position: absolute;
    left: 37px;
    top: 37px;
    width: 775px;
    height: 1126px;
    overflow: hidden;
    background: radial-gradient(ellipse 62% 48% at 52% 47%, var(--sun-orange) 0%, #ee7424 35%, var(--warm-red) 72%, var(--deep-red) 100%);
  }
  .poster__foliage,
  .headline {
    position: absolute;
    inset: 0;
    width: 100%;
    height: 100%;
    margin: 0;
  }
  .headline__word {
    font-family: "Chewy", "Comic Sans MS", "Arial Rounded MT Bold", sans-serif;
    font-weight: 700;
    fill: var(--headline-yellow);
  }
  .offer {
    position: absolute;
    left: 0;
    width: 100%;
    margin: 0;
    text-align: center;
    color: var(--text-white);
    line-height: 1;
    white-space: nowrap;
  }
  .offer--days {
    top: 442px;
    font-weight: 700;
    font-size: 46px;
    letter-spacing: 2px;
  }
  .offer--price {
    top: 506px;
    font-weight: 700;
    font-size: 112px;
    color: var(--headline-yellow);
    letter-spacing: 4px;
  }
  .offer--drinks {
    top: 649px;
    font-weight: 700;
    font-style: italic;
    font-size: 44px;
    line-height: 62px;
    letter-spacing: 3px;
  }
  .offer--hours {
    top: 952px;
    font-weight: 700;
    font-size: 46px;
    letter-spacing: 3px;
  }
  .offer--extras {
    top: 1008px;
    font-weight: 400;
    font-size: 44px;
    letter-spacing: 1px;
  }
</style>
</head>
<body>
  <main class="poster">
    <div class="poster__panel">
      <svg class="poster__foliage" viewBox="0 0 775 1126" role="img" aria-label="Tropical palm and fern leaf silhouettes framing the poster">
        <defs>
          <radialGradient id="foliage-top" cx="0.5" cy="0.5" r="0.5">
            <stop offset="0" stop-color="#a8182c" stop-opacity="0.75"/>
            <stop offset="1" stop-color="#a8182c" stop-opacity="0"/>
          </radialGradient>
          <radialGradient id="foliage-low" cx="0.5" cy="0.5" r="0.5">
            <stop offset="0" stop-color="#b51c30" stop-opacity="0.7"/>
            <stop offset="1" stop-color="#b51c30" stop-opacity="0"/>
          </radialGradient>
        </defs>
        <ellipse cx="560" cy="170" rx="360" ry="260" fill="url(#foliage-top)"/>
        <ellipse cx="90" cy="760" rx="260" ry="430" fill="url(#foliage-low)"/>
        <ellipse cx="430" cy="1080" rx="460" ry="200" fill="url(#foliage-low)"/>
        <ellipse cx="740" cy="900" rx="180" ry="260" fill="url(#foliage-low)"/>
      </svg>

      <h1 class="headline">
        <svg viewBox="0 0 775 1126" width="775" height="1126" aria-label="Cheap Drinks">
          <text class="headline__word" x="28" y="205" font-size="175" textLength="440" lengthAdjust="spacingAndGlyphs" transform="rotate(-7 28 205)">CheAP</text>
          <text class="headline__word" x="228" y="338" font-size="170" textLength="505" lengthAdjust="spacingAndGlyphs" transform="rotate(-5.5 228 338)">DRINKS</text>
        </svg>
      </h1>

      <p class="offer offer--days">Thursday &amp; Friday</p>
      <p class="offer offer--price">JUST $3.50</p>
      <p class="offer offer--drinks">Schooners of Local Beer<br>or Glass of House<br>Wine &amp; Bubbly</p>

      <p class="offer offer--hours">From 3.30pm to 6.30 pm</p>
      <p class="offer offer--extras">Nibblies Provided</p>
    </div>
  </main>
</body>
</html>
```